Word document template for sales proposals

I am after a template that is simple but impactful. Use of colour to be limited but some for impact would be good. The proposals are for use in the professional technical field.

```html
<!DOCTYPE html>
<html lang="en">
<head>
<meta charset="utf-8">
<title>Proposal Cover</title>
<link rel="stylesheet" href="https://fonts.googleapis.com/css2?family=Open+Sans:wght@400;700;800&display=swap">
<style>
  :root {
    --paper: #ffffff;
    --title-blue: #1f4e79;
    --ink-navy: #2b3566;
    --brand-orange: #f39322;
    --brand-sky: #2aa8e0;
    --leaf-light: #7fbf3f;
    --leaf-mid: #4f9a2a;
    --leaf-deep: #1f4a1c;
    --leaf-shadow: #0f2612;
    --date-white: #ffffff;
  }
  * { margin: 0; padding: 0; box-sizing: border-box; }
  html, body {
    width: 1200px;
    height: 849px;
    overflow: hidden;
    background: var(--paper);
  }
  .cover {
    position: relative;
    width: 1200px;
    height: 849px;
    font-family: "Open Sans", Arial, sans-serif;
    color: var(--ink-navy);
    background: var(--paper);
    overflow: hidden;
  }
  .brand {
    position: absolute;
    left: 37px;
    top: 62px;
    display: flex;
    align-items: center;
    gap: 10px;
  }
  .brand-dot {
    width: 34px;
    height: 34px;
    border-radius: 50%;
    background: var(--brand-sky);
  }
  .brand-name {
    font-size: 28px;
    font-weight: 700;
    color: var(--brand-orange);
    letter-spacing: 0.5px;
  }
  .cover-title {
    position: absolute;
    left: 72px;
    top: 200px;
    font-size: 92px;
    font-weight: 800;
    line-height: 1.2;
    color: var(--title-blue);
    letter-spacing: 1px;
    text-shadow: 1px 2px 2px rgba(0, 0, 0, 0.25);
  }
  .centered {
    position: absolute;
    transform: translateX(-50%);
    white-space: nowrap;
    text-align: center;
  }
  .project-name {
    left: 281px;
    top: 343px;
    font-size: 28px;
    font-weight: 400;
  }
  .label {
    font-size: 20px;
    font-weight: 400;
  }
  .value {
    font-size: 20px;
    font-weight: 700;
  }
  .prepared-for-label { left: 281px; top: 475px; }
  .client-name        { left: 281px; top: 523px; }
  .prepared-by-label  { left: 290px; top: 629px; }
  .author-name        { left: 290px; top: 676px; }
  .author-email       { left: 290px; top: 708px; }
  .cover-photo {
    position: absolute;
    left: 617px;
    top: 0;
    width: 583px;
    height: 849px;
    background:
      radial-gradient(ellipse 60% 45% at 55% 50%, var(--leaf-light) 0%, var(--leaf-mid) 45%, transparent 80%),
      radial-gradient(ellipse 70% 40% at 70% 10%, #3f6e35 0%, transparent 70%),
      linear-gradient(180deg, #2f5a2a 0%, var(--leaf-deep) 30%, #3c7a25 55%, var(--leaf-deep) 80%, var(--leaf-shadow) 100%);
  }
  .cover-date {
    position: absolute;
    left: 933px;
    top: 647px;
    transform: translateX(-50%);
    font-size: 34px;
    font-weight: 700;
    color: var(--date-white);
    white-space: nowrap;
  }
</style>
</head>
<body>
  <main class="cover">
    <div class="brand">
      <span class="brand-dot"></span>
      <span class="brand-name">Verdant Works</span>
    </div>

    <h1 class="cover-title">PROPOSAL</h1>

    <p class="centered project-name">Project name</p>

    <p class="centered label prepared-for-label">Prepared for</p>
    <p class="centered value client-name">Brightfield Studios</p>

    <p class="centered label prepared-by-label">Prepared by</p>
    <p class="centered value author-name">Morgan Hale</p>
    <p class="centered value author-email">morgan@northvane.com</p>

    <div class="cover-photo" role="img" aria-label="Close-up photograph of a green leaf with a single water droplet at its centre"></div>
    <p class="cover-date">October 19, 2023</p>
  </main>
</body>
</html>
```